Bref créative
Stationary (Branding) for Plumbing & Heating Buisness
Dorrick Haines Ltd
Use same font as used in my logo
Dorrick Haines
Unit 8 Larchmoor Ind Est.
Cwmbrellog
Tregarvon
Glynmorth
dorrick@greenvoltaria.co.uk
www.dorrickhaines.com
Looking for complete stationary with A4 letter head, business cards and so on using the logo provided. Modern, clean and eco friendly is the image we are looking for.
The font used in the logo is not final and maybe changed so please ignore that.
Would like to see the logo on the back of the card with spot UV effect.
The font in this logo is not final and may change
plumbing
renewables
heating

```html
<!DOCTYPE html>
<html lang="en">
<head>
<meta charset="utf-8">
<title>Dorrick Haines Ltd – Business Card</title>
<link href="https://fonts.googleapis.com/css2?family=Open+Sans:wght@400;600;700&display=swap" rel="stylesheet">
<style>
  :root {
    --backdrop: #e9e7e3;
    --card-white: #ffffff;
    --band-dark: #2f2f31;
    --accent-green: #6cbf3a;
    --logo-grey: #4a4a4c;
    --text-light: #f2f2f2;
  }
  * { box-sizing: border-box; margin: 0; padding: 0; }
  html, body {
    width: 1200px;
    height: 900px;
    overflow: hidden;
    background: var(--backdrop);
    font-family: "Open Sans", Arial, sans-serif;
  }
  .canvas {
    position: relative;
    width: 1200px;
    height: 900px;
  }
  .business-card {
    position: absolute;
    left: 100px;
    top: 165px;
    width: 1000px;
    height: 570px;
    background: var(--card-white);
    box-shadow: 0 10px 30px rgba(0,0,0,0.18);
    overflow: hidden;
  }
  .brand {
    position: absolute;
    left: 230px;
    top: 62px;
    display: flex;
    align-items: center;
    gap: 20px;
  }
  .brand-dot {
    width: 58px;
    height: 58px;
    border-radius: 50%;
    background: var(--accent-green);
  }
  .brand-name {
    font-size: 46px;
    font-weight: 400;
    color: var(--logo-grey);
    letter-spacing: -0.5px;
    white-space: nowrap;
  }
  .info-band {
    position: absolute;
    left: 0;
    top: 178px;
    width: 100%;
    height: 302px;
    background: var(--band-dark);
  }
  .name-marker {
    position: absolute;
    left: 0;
    top: 212px;
    width: 14px;
    height: 52px;
    background: var(--accent-green);
  }
  .person-name {
    position: absolute;
    left: 40px;
    top: 222px;
    font-size: 22px;
    font-weight: 700;
    color: var(--text-light);
    white-space: nowrap;
  }
  .contact-list {
    position: absolute;
    left: 570px;
    top: 26px;
    list-style: none;
    color: var(--text-light);
    font-size: 19px;
    line-height: 1.3;
  }
  .contact-list li {
    display: flex;
    align-items: flex-start;
    gap: 12px;
    margin-bottom: 4px;
    white-space: nowrap;
  }
  .contact-icon {
    flex: 0 0 20px;
    width: 20px;
    height: 20px;
    margin-top: 3px;
  }
</style>
</head>
<body>
<main class="canvas">
  <section class="business-card">
    <div class="brand">
      <span class="brand-dot"></span>
      <span class="brand-name">Dorrick Haines Ltd.</span>
    </div>

    <div class="info-band">
      <div class="name-marker"></div>
      <p class="person-name">Dorrick Haines</p>

      <ul class="contact-list">
        <li>
          <svg class="contact-icon" viewBox="0 0 20 20"><circle cx="10" cy="10" r="10" fill="#f2f2f2"/><path d="M5 10.5 10 6l5 4.5h-1.6V14h-2.4v-2.6H9V14H6.6v-3.5z" fill="#2f2f31"/></svg>
          <span>Unit 8 Larchmoor Ind Est.<br>Cwmbrellog Tregarvon Glynmorth</span>
        </li>
        <li>
          <svg class="contact-icon" viewBox="0 0 20 20"><circle cx="10" cy="10" r="10" fill="#f2f2f2"/><path d="M7 5.5l1.6 2.3-1 1.1a6 6 0 0 0 3.5 3.5l1.1-1 2.3 1.6-.9 1.6c-3.9-.3-7.1-3.5-7.4-7.4z" fill="#2f2f31"/></svg>
          <span>01632 960418</span>
        </li>
        <li>
          <svg class="contact-icon" viewBox="0 0 20 20"><circle cx="10" cy="10" r="10" fill="#f2f2f2"/><rect x="7" y="4.5" width="6" height="11" rx="1" fill="#2f2f31"/><rect x="8" y="6" width="4" height="6.5" fill="#f2f2f2"/></svg>
          <span>01632 960752</span>
        </li>
        <li>
          <svg class="contact-icon" viewBox="0 0 20 20"><circle cx="10" cy="10" r="10" fill="#f2f2f2"/><rect x="5" y="6.5" width="10" height="7" fill="#2f2f31"/><path d="M5 6.5l5 4 5-4" fill="none" stroke="#f2f2f2" stroke-width="1"/></svg>
          <span>dorrick@greenvoltaria.co.uk</span>
        </li>
        <li>
          <svg class="contact-icon" viewBox="0 0 20 20"><circle cx="10" cy="10" r="10" fill="#f2f2f2"/><circle cx="10" cy="10" r="5" fill="none" stroke="#2f2f31" stroke-width="1.3"/><path d="M5 10h10M10 5c-2.2 2.8-2.2 7.2 0 10M10 5c2.2 2.8 2.2 7.2 0 10" fill="none" stroke="#2f2f31" stroke-width="1.1"/></svg>
          <span>www.dorrickhaines.com</span>
        </li>
      </ul>
    </div>
  </section>
</main>
</body>
</html>
```